St. Paddy’s Day Invitation

Invitation to text to people:
6th Annual St. Paddy’s Day Party
Where: The Halvorsen’s
When: Saturday, March 25
Acoustic session by Tavin Ashcombe from Mr. Paperlanterns
Fundraiser for Otis Wembley ‘Steady Compass’ Fund

Target Market(s)

Adults only, all friends from our town, Moorestown, NJ

Colors
00AB8E
00BBA5
67D7C9
C6EFE9
E9F9F6
59FF00
82FF00
B8FF75
E3FFCB
F4FFEA

```html
<!DOCTYPE html>
<html lang="en">
<head>
<meta charset="UTF-8">
<title>6th Annual St. Paddy’s Day Party</title>
<link rel="stylesheet" href="https://fonts.googleapis.com/css2?family=Poppins:wght@400;600;700;800&family=Sacramento&family=Yellowtail&display=swap">
<style>
  :root {
    --bg-deep: #081a0b;
    --bg-mid: #173d19;
    --bg-glow: #24552a;
    --white: #ffffff;
    --gold: #f6c324;
    --gold-box: #f9c52f;
    --ink-dark: #1b1b10;
    --neon-cream: #fbf7b8;
    --neon-yellow: #e9e43a;
    --neon-lime: #e3ffcb;
    --neon-green: #82ff00;
    --clover: #2f7a38;
    --clover-dark: #1f5a27;
    --stage-teal: #1fa98f;
  }
  * { margin: 0; padding: 0; box-sizing: border-box; }
  html, body { width: 675px; height: 1200px; overflow: hidden; background: var(--bg-deep); }
  .invite {
    position: relative;
    width: 675px; height: 1200px; overflow: hidden;
    background: radial-gradient(ellipse 70% 55% at 50% 32%, var(--bg-glow) 0%, var(--bg-mid) 40%, var(--bg-deep) 100%);
    font-family: 'Poppins', sans-serif;
    color: var(--white);
  }
  .edition { position: absolute; left: 180px; top: 130px; width: 315px; height: 100px; }
  .edition text { font-family: 'Poppins', sans-serif; font-weight: 800; font-size: 38px; fill: var(--white); }
  .neon {
    position: absolute; left: 0; width: 675px; text-align: center;
    font-family: 'Sacramento', cursive; font-weight: 400; line-height: 1;
  }
  .neon-1 { top: 195px; font-size: 142px; color: var(--neon-cream); text-shadow: 0 0 6px var(--neon-yellow), 0 0 18px var(--neon-yellow), 0 0 34px rgba(233,228,58,.6); }
  .neon-2 { top: 335px; left: -8px; font-size: 142px; color: #f2f8b0; text-shadow: 0 0 6px #d8ea3a, 0 0 18px #c8e83a, 0 0 34px rgba(184,255,117,.55); }
  .neon-3 { top: 470px; left: 10px; font-size: 150px; color: var(--neon-lime); text-shadow: 0 0 6px #b8ff75, 0 0 18px var(--neon-green), 0 0 34px rgba(130,255,0,.55); }
  .tagline {
    position: absolute; top: 672px; left: 0; width: 675px; text-align: center;
    font-family: 'Yellowtail', cursive; font-size: 52px; color: var(--gold); line-height: 1;
  }
  .venue {
    position: absolute; top: 720px; left: 100px; width: 460px; text-align: center;
    font-weight: 700; font-size: 15.5px; line-height: 25px; text-transform: uppercase; letter-spacing: .2px;
  }
  .date {
    position: absolute; top: 784px; left: 182px; width: 312px; height: 33px;
    background: var(--gold-box); border-radius: 3px;
    color: var(--ink-dark); font-weight: 700; font-size: 17.5px; line-height: 33px; text-align: center;
  }
  .stage-photo {
    position: absolute; left: 318px; top: 808px; width: 357px; height: 222px;
    background: radial-gradient(ellipse at 60% 25%, #4fd3bd 0%, var(--stage-teal) 25%, #0f4d3d 60%, #061a14 100%);
    clip-path: polygon(6% 30%, 30% 8%, 62% 0, 100% 3%, 100% 100%, 40% 100%, 26% 86%, 0 70%);
  }
  .clover { position: absolute; border-radius: 50%; background: radial-gradient(circle, var(--clover) 0%, var(--clover-dark) 70%); }
  .clover-left { left: -20px; top: 405px; width: 150px; height: 175px; opacity: .85; }
  .clover-right { left: 512px; top: 905px; width: 165px; height: 180px; }
  .party-horn {
    position: absolute; left: 505px; top: 540px; width: 90px; height: 105px;
    background: linear-gradient(135deg, #e8d43a 0%, #2c8a3a 100%);
    clip-path: polygon(20% 0, 100% 60%, 10% 100%);
  }
  .performer {
    position: absolute; top: 887px; left: 46px; width: 270px;
    font-weight: 700; font-size: 18.5px; line-height: 27.5px; text-transform: uppercase;
  }
  .fundraiser { position: absolute; top: 1046px; left: 0; width: 675px; text-align: center; }
  .fundraiser-lead { font-weight: 400; font-size: 18px; text-transform: uppercase; letter-spacing: .3px; line-height: 26px; }
  .fundraiser-name { margin-top: 6px; font-weight: 700; font-size: 21px; color: var(--gold); text-transform: uppercase; letter-spacing: .3px; }
</style>
</head>
<body>
<main class="invite">
  <div class="party-horn" role="img" aria-label="Striped party horn with streamers"></div>
  <div class="clover clover-left" role="img" aria-label="Green shamrock illustration"></div>

  <svg class="edition" viewBox="0 0 315 100" aria-label="6th Annual">
    <defs><path id="edition-arc" d="M 10 95 Q 157 -5 305 95"/></defs>
    <text><textPath href="#edition-arc" startOffset="50%" text-anchor="middle">6TH ANNUAL</textPath></text>
  </svg>

  <h1>
    <span class="neon neon-1">St. Paddy’s</span>
    <span class="neon neon-2">Day</span>
    <span class="neon neon-3">Party!</span>
  </h1>

  <p class="tagline">Music &amp; Beer</p>
  <p class="venue">Join us for a St. Paddy's Day party at the Halvorsen's</p>
  <p class="date">MARCH 25,2023 (SATURDAY)</p>

  <div class="stage-photo" role="img" aria-label="Photo of a live band performing on a teal-lit stage"></div>
  <div class="clover clover-right" role="img" aria-label="Green shamrock illustration"></div>

  <p class="performer">Acoustic session by Tavin Ashcombe from Mr. Paperlanterns</p>

  <div class="fundraiser">
    <p class="fundraiser-lead">A fundraising event for</p>
    <p class="fundraiser-name">Otis Wembley ‘Steady Compass’ Fund</p>
  </div>
</main>
</body>
</html>
```